Broschüre für Baumanagement
Zielgruppe
Baumanagement
Wir liefern von der Planung, über die notwendigen Handwerksfirmen langjährige Partner, Bauleitung alle notwenidgen Partner
Wir betreuen seit jahren Kunden aus dem Immobilienwesen, Handel usw.
Ein Ansprechpartner vond er Planung bis zur Übergabe
Aufgabenstellung
DIN A4, 2 Seiten, Modern, Fakten, Gerne nur in schwarz und weiss halten

```html
<!DOCTYPE html>
<html lang="de">
<head>
<meta charset="utf-8">
<title>Nordhaus Group – Baumanagement Broschüre</title>
<link rel="stylesheet" href="https://fonts.googleapis.com/css2?family=Montserrat:wght@400;500;600;700;800&display=swap">
<style>
  :root {
    --ink: #0b0b0b;
    --paper: #ffffff;
    --stage: #d9d9d9;
    --mist: #c9c9c9;
    --slate: #3a3a3a;
    --photo-light: #b4b4b4;
    --photo-dark: #4a4a4a;
  }
  * { margin: 0; padding: 0; box-sizing: border-box; }
  html, body { width: 906px; height: 1200px; overflow: hidden; }
  body {
    background: var(--stage);
    font-family: "Montserrat", sans-serif;
    color: var(--ink);
    display: flex;
    align-items: center;
    justify-content: center;
    gap: 16px;
  }
  .page {
    position: relative;
    width: 430px;
    height: 608px;
    background: var(--paper);
    overflow: hidden;
    box-shadow: 0 10px 30px rgba(0,0,0,.3);
  }
  .page-shapes { position: absolute; inset: 0; width: 100%; height: 100%; }
  .block { position: absolute; left: 0; right: 0; text-align: center; }

  /* back page */
  .service-title { top: 36px; font-size: 17px; font-weight: 700; }
  .service-text { top: 64px; font-size: 11px; line-height: 15px; padding: 0 50px; font-weight: 500; }
  .contact-banner {
    top: 122px; left: 44px; right: 62px; height: 30px;
    background: var(--ink); color: var(--paper);
    clip-path: polygon(2% 0, 100% 0, 98% 100%, 0 100%);
    font-size: 14px; font-weight: 700; line-height: 30px;
  }
  .phone {
    top: 158px; font-size: 31px; font-weight: 700; letter-spacing: .5px;
    display: flex; justify-content: center; align-items: center; gap: 8px;
  }
  .phone svg { width: 24px; height: 24px; }
  .web-spaced { top: 200px; font-size: 13px; letter-spacing: 4.5px; font-weight: 500; }
  .brand { line-height: 1; }
  .brand-name { font-weight: 700; display: block; }
  .brand-sub { font-weight: 700; display: block; letter-spacing: 1.5px; }
  .brand-small { top: 232px; }
  .brand-small .brand-name { font-size: 17px; }
  .brand-small .brand-sub { font-size: 5.5px; margin-top: 4px; }

  /* front page */
  .brand-large { top: 56px; }
  .brand-large .brand-name { font-size: 24px; }
  .brand-large .brand-sub { font-size: 7px; margin-top: 6px; }
  .intro { top: 165px; color: var(--paper); font-size: 11px; line-height: 14px; font-weight: 500; }
  .claim { top: 208px; color: var(--paper); font-size: 17px; line-height: 21px; font-weight: 700; }
  .web-tab {
    position: absolute; left: 112px; width: 208px; bottom: 0; height: 40px;
    background: var(--paper); border-radius: 10px 10px 0 0;
    font-size: 14px; font-weight: 700; text-align: center; line-height: 40px;
  }
</style>
</head>
<body>

  <section class="page page-back" aria-label="Rückseite">
    <svg class="page-shapes" viewBox="0 0 430 608" preserveAspectRatio="none">
      <defs>
        <linearGradient id="officeToneA" x1="0" y1="0" x2="1" y2="1">
          <stop offset="0" stop-color="var(--photo-light)"/>
          <stop offset="1" stop-color="var(--photo-dark)"/>
        </linearGradient>
      </defs>
      <polygon points="0,318 430,302 430,310 0,352" fill="var(--mist)"/>
      <polygon points="0,352 430,296 430,308 0,364" fill="var(--ink)"/>
      <polygon points="0,370 430,314 430,608 0,608" fill="url(#officeToneA)" role="img" aria-label="Photo of a modern glass-walled meeting room with office chairs"/>
    </svg>
    <h2 class="block service-title">Baumanagement</h2>
    <p class="block service-text">Wir liefern von der Planung, über die notwendigen Handwerksfirmen langjährige Partner, Bauleitung alle notwenidgen Partner</p>
    <div class="block contact-banner">Kontaktieren Sie uns</div>
    <div class="block phone">
      <svg viewBox="0 0 24 24" aria-hidden="true"><circle cx="12" cy="12" r="12" fill="var(--ink)"/><path d="M8.5 6.5l2 2.2-1.2 1.6c.8 1.7 2 2.9 3.6 3.7l1.6-1.2 2.2 2-1.2 2c-4.6-.4-8.8-4.6-9-9.2z" fill="var(--paper)"/></svg>
      <span>040-555-0199</span>
    </div>
    <div class="block web-spaced">www.nordhaus-immo.de</div>
    <div class="block brand brand-small">
      <span class="brand-name">NORDHAUS GROUP</span>
      <span class="brand-sub">REAL ESTATE INVESTMENT</span>
    </div>
  </section>

  <section class="page page-front" aria-label="Titelseite">
    <svg class="page-shapes" viewBox="0 0 430 608" preserveAspectRatio="none">
      <defs>
        <linearGradient id="officeToneB" x1="0" y1="0" x2="1" y2="1">
          <stop offset="0" stop-color="var(--photo-light)"/>
          <stop offset="1" stop-color="var(--photo-dark)"/>
        </linearGradient>
      </defs>
      <path d="M0,100 L150,130 Q215,145 280,128 L430,92 L430,350 L0,350 Z" fill="var(--mist)"/>
      <path d="M0,106 L150,136 Q215,150 280,134 L430,98 L430,350 L0,350 Z" fill="var(--ink)"/>
      <polygon points="260,280 430,265 430,340" fill="var(--slate)"/>
      <path d="M0,298 Q160,278 270,292 L430,336 L430,608 L0,608 Z" fill="url(#officeToneB)" stroke="var(--paper)" stroke-width="6" role="img" aria-label="Photo of a conference table with chairs in a high-rise office"/>
    </svg>
    <div class="block brand brand-large">
      <span class="brand-name">NORDHAUS GROUP</span>
      <span class="brand-sub">REAL ESTATE INVESTMENT</span>
    </div>
    <p class="block intro">WE HAVE BEEN A REAL ESTATE CONSULTANCY<br>FOR MANY YEARS.</p>
    <p class="block claim">WE ADVISE AND MEDIATE PRIMARILY<br>IN THE COMMERCIAL AND<br>RESIDENTIAL ASSET CLASSES.</p>
    <div class="web-tab">www.nordhaus-immo.de</div>
  </section>

</body>
</html>
```